Saffron Ledger Works Flyer

We need a one page promotional piece that explains what our company does, and the benefits it provides in a simple, elegant, easy to understand way. I would like to print it on glossy heavyweight paper to give a feel of high quality and legitimacy. I will include the logo, the tag line, and the main benefits that the company offers.

Tag line concept, may not need these exact words. "Give us 5 minutes a day, and we will help you build a Saffron Ledger Works."

Key points...(exact wording not required if you think of a better way to say it)

Software easy enough for my grandpa to use.
Lets you use snail mail, email, texting, and social media to quickly market to your customers at very low cost.
Web based which allows you to launch media campaigns from your desktop, or smartphone in moments.
Quick 3 - 5 minute training videos which give you hard hitting, quick action tips that will help you make your business better today.
Live coaching calls to help motivate you to improve your business.
No contracts, or start up fees. One low price of $299 per month.

Restaurant owners

Restaurant

```html
<!DOCTYPE html>
<html lang="en">
<head>
<meta charset="utf-8">
<title>Saffron Ledger Works Flyer</title>
<link rel="stylesheet" href="https://fonts.googleapis.com/css2?family=Arvo:wght@700&family=Open+Sans:wght@400;600&display=swap">
<style>
  :root {
    --stage: #d9d8d4;
    --sky: #a5c3e6;
    --lime: #9cc823;
    --lime-deep: #2f9a3a;
    --silver: #c9cbcd;
    --orange: #f15a24;
    --ink-grey: #5b5c5e;
    --mark-grey: #c4c6c8;
    --white: #ffffff;
  }
  * { margin: 0; padding: 0; box-sizing: border-box; }
  html, body {
    width: 1200px; height: 1000px; overflow: hidden;
    background: var(--stage);
  }
  .flyer {
    position: absolute; left: 275px; top: 40px;
    width: 650px; height: 920px;
    background: var(--sky);
    overflow: hidden;
    font-family: "Open Sans", Arial, sans-serif;
  }
  .flyer-shapes { position: absolute; inset: 0; }
  .headline, .offer {
    position: absolute; left: 0; width: 100%;
    text-align: center; color: var(--white);
    font-family: "Arvo", Georgia, serif; font-weight: 700;
    text-shadow: 0 2px 2px rgba(0,0,0,.35);
    line-height: 1.05;
  }
  .headline { top: 8px; font-size: 33px; padding-left: 34px; }
  .offer { top: 830px; font-size: 33px; }
  .brand {
    position: absolute; left: 0; top: 110px; width: 100%;
    display: flex; flex-direction: column; align-items: center;
  }
  .brand-dot {
    width: 190px; height: 190px; border-radius: 50%;
    background: var(--mark-grey);
    margin-left: 60px;
  }
  .brand-name {
    margin-top: 34px; margin-left: 60px;
    font-family: "Arvo", Georgia, serif; font-weight: 700;
    color: var(--ink-grey); font-size: 34px; line-height: 1;
    text-transform: uppercase; letter-spacing: 1px; text-align: center;
  }
  .benefits {
    position: absolute; left: 100px; top: 470px; width: 500px;
    list-style: none;
    transform: rotate(2.2deg); transform-origin: left top;
  }
  .benefit {
    display: flex; align-items: flex-start; gap: 18px;
    color: var(--white); font-size: 15px; line-height: 1.3;
    margin-bottom: 20px;
  }
  .benefit-icon { flex: 0 0 40px; height: 40px; }
  .benefit-text { padding-top: 4px; }
</style>
</head>
<body>
<main class="flyer">
  <svg class="flyer-shapes" width="650" height="920" viewBox="0 0 650 920" aria-hidden="true">
    <defs>
      <linearGradient id="band" x1="0" x2="1">
        <stop offset="0" stop-color="#a6cf2a"/>
        <stop offset=".5" stop-color="#6fb22e"/>
        <stop offset="1" stop-color="#a6cf2a"/>
      </linearGradient>
      <linearGradient id="band-low" x1="0" x2="1">
        <stop offset="0" stop-color="#a6cf2a"/>
        <stop offset=".5" stop-color="var(--lime-deep)"/>
        <stop offset="1" stop-color="#a6cf2a"/>
      </linearGradient>
    </defs>
    <path d="M0 0H650V112Q330 95 0 124Z" fill="url(#band)"/>
    <path d="M0 124Q330 95 650 112" fill="none" stroke="var(--silver)" stroke-width="5"/>
    <polygon points="90,455 589,495 607,830 36,830" fill="var(--orange)"/>
    <path d="M0 826Q330 812 650 826V920H0Z" fill="url(#band-low)"/>
    <path d="M0 826Q330 812 650 826" fill="none" stroke="var(--silver)" stroke-width="5"/>
  </svg>

  <h1 class="headline">Give us 5 minutes a day,<br>and we will help you build a</h1>

  <div class="brand">
    <span class="brand-dot"></span>
    <p class="brand-name">Saffron<br>Ledger<br>Works</p>
  </div>

  <ul class="benefits">
    <li class="benefit">
      <svg class="benefit-icon" viewBox="0 0 40 40"><rect x="4" y="6" width="32" height="26" rx="2" fill="var(--white)"/><circle cx="26" cy="19" r="7" fill="var(--orange)"/><circle cx="26" cy="19" r="2" fill="var(--white)"/></svg>
      <span class="benefit-text">Software easy enough for my grandpa to use.</span>
    </li>
    <li class="benefit">
      <svg class="benefit-icon" viewBox="0 0 40 40"><rect x="5" y="10" width="30" height="21" rx="2" fill="var(--white)"/><path d="M6 12L20 23L34 12" fill="none" stroke="var(--orange)" stroke-width="2.5"/></svg>
      <span class="benefit-text">Lets you use snail mail, email, texting, and social media to quickly market to your customers at very low cost.</span>
    </li>
    <li class="benefit">
      <svg class="benefit-icon" viewBox="0 0 40 40"><rect x="5" y="6" width="30" height="21" rx="2" fill="none" stroke="var(--white)" stroke-width="4"/><rect x="17" y="27" width="6" height="6" fill="var(--white)"/><rect x="11" y="32" width="18" height="3" fill="var(--white)"/></svg>
      <span class="benefit-text">Web based which allows you to launch media campaigns from your desktop, or smartphone in moments.</span>
    </li>
    <li class="benefit">
      <svg class="benefit-icon" viewBox="0 0 40 40"><circle cx="20" cy="20" r="17" fill="var(--white)"/><circle cx="20" cy="20" r="12" fill="var(--orange)"/><path d="M20 12V21H27" fill="none" stroke="var(--white)" stroke-width="3"/></svg>
      <span class="benefit-text">Quick 3 - 5 minute training videos which give you hard hitting, quick action tips that will help you make your business better today.</span>
    </li>
    <li class="benefit">
      <svg class="benefit-icon" viewBox="0 0 40 40"><path d="M7 22A13 13 0 0 1 33 22" fill="none" stroke="var(--white)" stroke-width="4"/><rect x="4" y="20" width="8" height="12" rx="3" fill="var(--white)"/><rect x="28" y="20" width="8" height="12" rx="3" fill="var(--white)"/><path d="M32 32Q30 37 22 37" fill="none" stroke="var(--white)" stroke-width="2.5"/></svg>
      <span class="benefit-text">Live coaching calls to help motivate you to improve your business.</span>
    </li>
  </ul>

  <p class="offer">No contracts, or start up fees.<br>One low price of $299 per month.</p>
</main>
</body>
</html>
```